Healthcare marketing Website design

This is for a healthcare marketing agency
All details and brief included in the files

I need the design to be incredible!

5 pages to be designed
Home page
About
Portfolio Page
Services
Start your project page

If you need more stock images - download preview images from kestrine pix so I can purchase at a later date

```html
<!DOCTYPE html>
<html lang="en">
<head>
<meta charset="utf-8">
<title>Northbeam Consulting — Home</title>
<link rel="stylesheet" href="https://fonts.googleapis.com/css2?family=Comfortaa:wght@400;500&family=Poppins:wght@400;600&display=swap">
<style>
  :root {
    --ink: #1f2b55;
    --nav: #4b5066;
    --accent: #12a4e2;
    --lilac: #e7c6f5;
    --lilac-soft: #efe0fa;
    --social: #2b2d3a;
    --social-text: #ffffff;
    --bg-top: #ffffff;
    --bg-mid: #f2f5fd;
    --bg-end: #d7defc;
  }
  * { margin: 0; padding: 0; box-sizing: border-box; }
  html, body { width: 1200px; height: 892px; overflow: hidden; }
  body {
    position: relative;
    background:
      radial-gradient(ellipse 60% 50% at 0% 100%, #e3edfd 0%, transparent 70%),
      linear-gradient(150deg, var(--bg-top) 0%, var(--bg-top) 30%, var(--bg-mid) 60%, var(--bg-end) 100%);
    font-family: "Poppins", sans-serif;
    color: var(--ink);
  }
  .hero-decor {
    position: absolute; left: 0; top: 520px; width: 1200px; height: 372px;
    background:
      radial-gradient(ellipse 30% 45% at 28% 55%, var(--lilac-soft) 0%, transparent 70%),
      radial-gradient(ellipse 25% 50% at 88% 45%, var(--lilac-soft) 0%, transparent 70%),
      radial-gradient(ellipse 45% 30% at 55% 95%, var(--lilac) 0%, transparent 70%);
    opacity: .7;
  }
  .site-header {
    position: absolute; top: 50px; left: 96px; right: 128px;
    display: flex; align-items: center; justify-content: space-between;
  }
  .brand {
    display: flex; align-items: center; gap: 10px;
    font-family: "Comfortaa", sans-serif; font-weight: 500;
    color: var(--accent); text-decoration: none;
  }
  .brand-dot { width: 30px; height: 30px; border-radius: 50%; background: var(--accent); }
  .brand-name { font-size: 25px; line-height: 1; }
  .brand-name small { display: block; font-size: 9px; letter-spacing: .8px; text-align: right; margin-top: 2px; }
  .main-nav { display: flex; gap: 31px; }
  .main-nav a { font-size: 15px; color: var(--nav); text-decoration: none; }
  .hero-title {
    position: absolute; top: 272px; left: 0; right: 0;
    width: 500px; margin: 0 auto; text-align: center;
    font-family: "Comfortaa", sans-serif; font-weight: 400;
    font-size: 43px; line-height: 1.18; color: var(--ink);
  }
  .cta {
    position: absolute; top: 549px; left: 0; right: 0; margin: 0 auto; width: 170px;
    display: flex; align-items: center; gap: 8px;
    font-weight: 600; font-size: 16px; color: var(--accent); text-decoration: none;
  }
  .cta-icon { width: 36px; height: 36px; }
  .social-links { position: absolute; left: 96px; top: 723px; display: flex; gap: 8px; }
  .social-links a {
    width: 34px; height: 34px; border-radius: 50%; background: var(--social);
    box-shadow: 0 4px 8px rgba(30,30,60,.25);
    display: flex; align-items: center; justify-content: center;
    font-size: 9px; font-weight: 600; color: var(--social-text); text-decoration: none;
  }
  .scroll-cue { position: absolute; left: 1010px; top: 650px; width: 30px; height: 70px; }
</style>
</head>
<body>
  <div class="hero-decor" role="img" aria-label="Soft lilac flowing line pattern across the lower hero area"></div>

  <header class="site-header">
    <a class="brand" href="#">
      <span class="brand-dot"></span>
      <span class="brand-name">northbeam<small>CONSULTING</small></span>
    </a>
    <nav class="main-nav">
      <a href="#">About</a>
      <a href="#">Portfolio</a>
      <a href="#">Contact Us</a>
      <a href="#">Our Services</a>
      <a href="#">Blog</a>
    </nav>
  </header>

  <h1 class="hero-title">Being online: a large opportunity for your practice</h1>

  <a class="cta" href="#">Start a project
    <svg class="cta-icon" viewBox="0 0 36 36" fill="none" stroke="var(--accent)" stroke-width="2" stroke-linecap="round" stroke-linejoin="round">
      <circle cx="18" cy="18" r="16.5"/>
      <path d="M10 18h16M20 12l6 6-6 6"/>
    </svg>
  </a>

  <div class="social-links">
    <a href="#">Lark</a>
    <a href="#">Hub</a>
    <a href="#">Pix</a>
  </div>

  <svg class="scroll-cue" viewBox="0 0 30 70" fill="none" stroke="var(--ink)" stroke-width="2" stroke-linecap="round" aria-label="Scroll down">
    <path d="M15 2v66M2 54l13 14 13-14"/>
  </svg>
</body>
</html>
```